I will ask the design of the business card

We are looking for business card design of the new company "VORTELL PAYWORKS STUDIO LLC." Based in Azerbaijan.
In case
We are working on Azerbaijan to set up the first exchange of crypto currencies.

The key currency used in exchanges is called "MIRTA".
In case
We are doing project to make crypto currency infrastructure.

We provide state-of-the-art technology to the world.

```html
<!DOCTYPE html>
<html lang="en">
<head>
<meta charset="utf-8">
<title>Vortell Payworks Studio LLC. – Business Card</title>
<link rel="stylesheet" href="https://fonts.googleapis.com/css2?family=Work+Sans:wght@400;500;700&display=swap">
<style>
  :root {
    --backdrop: #2e2826;
    --card-dark: #18191b;
    --card-light: #ffffff;
    --brand-blue: #1f6db5;
    --ink: #1c1c1c;
    --on-dark: #f2f2f2;
  }
  * { box-sizing: border-box; margin: 0; padding: 0; }
  html, body { width: 1200px; height: 715px; overflow: hidden; }
  body {
    background: var(--backdrop);
    font-family: "Work Sans", Arial, sans-serif;
    position: relative;
  }
  .card {
    position: absolute;
    top: 212px;
    width: 520px;
    height: 292px;
    border-radius: 3px;
    box-shadow: 0 10px 28px rgba(0,0,0,.45);
    overflow: hidden;
  }
  .card--front {
    left: 50px;
    background: var(--card-dark);
    border-bottom: 6px solid var(--brand-blue);
  }
  .card--back {
    left: 630px;
    background: var(--card-light);
  }
  .brand {
    position: absolute;
    display: flex;
    align-items: center;
    gap: 10px;
    white-space: nowrap;
    letter-spacing: .02em;
    font-weight: 400;
  }
  .brand__dot {
    width: 22px; height: 22px; border-radius: 50%;
    background: var(--brand-blue);
    flex: none;
  }
  .card--front .brand {
    left: 52px; top: 126px;
    font-size: 23px;
    color: var(--on-dark);
  }
  .card--back .brand {
    left: 22px; top: 124px;
    gap: 7px;
    font-size: 12px;
    letter-spacing: 0;
    color: var(--ink);
  }
  .card--back .brand .brand__dot { width: 13px; height: 13px; }
  .divider {
    position: absolute;
    left: 290px; top: 70px;
    width: 2px; height: 152px;
    background: var(--brand-blue);
  }
  .contact {
    position: absolute;
    left: 306px; top: 70px;
    width: 200px;
    color: var(--ink);
    font-size: 11px;
    line-height: 1.5;
    white-space: nowrap;
  }
  .contact__name {
    color: var(--brand-blue);
    font-weight: 700;
    font-size: 18px;
    letter-spacing: .04em;
    line-height: 1.1;
  }
  .contact__role { margin-bottom: 10px; }
  .contact__address { margin-bottom: 4px; }
  .contact__line { display: flex; align-items: center; gap: 7px; }
  .contact__line svg { width: 10px; height: 10px; flex: none; }
</style>
</head>
<body>
  <section class="card card--front">
    <div class="brand"><span class="brand__dot"></span>VORTELL PAYWORKS STUDIO LLC.</div>
  </section>

  <section class="card card--back">
    <div class="brand"><span class="brand__dot"></span>VORTELL PAYWORKS STUDIO LLC.</div>
    <div class="divider"></div>
    <div class="contact">
      <p class="contact__name">LEVAN OSTRID</p>
      <p class="contact__role">Founder</p>
      <p class="contact__address">AZ1010 , 8/3 Nerima str.<br>Baku city, Azerbaijan</p>
      <p class="contact__line">
        <svg viewBox="0 0 10 10" fill="none" stroke="#1f6db5" stroke-width="1.2"><rect x="2.5" y="0.8" width="5" height="8.4" rx="1"/><line x1="4.3" y1="7.6" x2="5.7" y2="7.6"/></svg>
        09055518734
      </p>
      <p class="contact__line">
        <svg viewBox="0 0 10 10" fill="#1f6db5"><path d="M2 1l2 2-1 1.2c.6 1.2 1.6 2.2 2.8 2.8L7 6l2 2-1.3 1.3C4.4 9 1 5.6.7 2.3z"/></svg>
        (+ 994 12) 555 01 47
      </p>
      <p class="contact__line">
        <svg viewBox="0 0 10 10" fill="none" stroke="#1f6db5" stroke-width="1.1"><rect x="0.8" y="2" width="8.4" height="6" rx=".6"/><path d="M1 2.4l4 3 4-3"/></svg>
        hello@vortellpayworks.com
      </p>
      <p class="contact__line">
        <svg viewBox="0 0 10 10" fill="none" stroke="#1f6db5" stroke-width="1"><circle cx="5" cy="5" r="4.2"/><ellipse cx="5" cy="5" rx="1.8" ry="4.2"/><line x1="0.8" y1="5" x2="9.2" y2="5"/></svg>
        vortellpayworks.com
      </p>
    </div>
  </section>
</body>
</html>
```